Help design website for "Civic Lantern Advisors" to advance the common good

Here is the Google doc link that lays out the design:

https://files.quorvinex.com/page/d/7TxRmWqa2ZbLkc9YhVnE4PdUs0GfJo3XiKv8Nt5Ry6Mw/edit?usp=sharing

Here is the Google drive folder with the logos and photos: https://store.quorvinex.com/open?id=4Kp9XmRtLwQ2bVnZc83Hs6YdJe0Fu

The testimonials are being gathered and will be shared by Friday, 1/4.

The winner will also have to migrate the coding files to my hosting site.

Thank you for your help! Looking forward to seeing your designs.

Target Market(s)

Prospective clients

Industry/Entity Type

Non Profit

Coding

Coded - Design and coding required

Number of Pages Required

5+ page

Requirements
Must have
• Noted in the Google doc regarding layout.
Nice to have

```html
<!DOCTYPE html>
<html lang="en">
<head>
<meta charset="utf-8">
<title>About Us – Civic Lantern Advisors</title>
<link rel="stylesheet" href="https://fonts.googleapis.com/css2?family=Montserrat:wght@400;500;600&display=swap">
<style>
  :root {
    --brand-blue: #4a9ad6;
    --header-bg: #f6f6f6;
    --ink: #333740;
    --body-text: #5a5d63;
    --divider: #ececec;
    --footer-bg: #2e333f;
    --white: #ffffff;
    --photo-warm: #b58a6c;
    --photo-cool: #8a8e93;
  }
  * { box-sizing: border-box; margin: 0; padding: 0; }
  html, body { width: 1015px; height: 1200px; overflow: hidden; background: var(--white); }
  body { font-family: "Montserrat", Arial, sans-serif; color: var(--body-text); }
  .page { position: relative; width: 1015px; height: 1200px; overflow: hidden; }

  .site-header { position: absolute; left: 0; top: 0; width: 1015px; height: 88px; background: var(--header-bg); }
  .brand { position: absolute; left: 68px; top: 24px; display: flex; align-items: center; gap: 10px; }
  .brand-square { width: 34px; height: 34px; background: var(--brand-blue); }
  .brand-name { font-size: 12.5px; font-weight: 500; letter-spacing: 3px; line-height: 15px; color: var(--ink); text-transform: uppercase; }
  .main-nav { position: absolute; top: 38px; left: 448px; display: flex; font-size: 9px; letter-spacing: 1.1px; font-weight: 500; color: var(--ink); text-transform: uppercase; }
  .main-nav a { color: inherit; text-decoration: none; margin-right: 30px; }
  .main-nav a.is-active { color: var(--brand-blue); }
  .contact-btn { position: absolute; left: 826px; top: 30px; width: 122px; height: 28px; border: 1px solid var(--brand-blue); color: var(--brand-blue); font-size: 9px; letter-spacing: 1.1px; font-weight: 500; display: flex; align-items: center; justify-content: center; text-transform: uppercase; }

  .accent-block { position: absolute; left: 0; top: 88px; width: 271px; height: 453px; background: var(--brand-blue); }
  .founder-photo { position: absolute; left: 68px; top: 149px; width: 270px; height: 325px; background: linear-gradient(160deg, var(--photo-cool) 0%, var(--photo-warm) 55%, #3b3132 100%); }

  .about { position: absolute; left: 372px; top: 144px; width: 572px; }
  .about h1 { font-size: 21px; font-weight: 500; color: var(--ink); letter-spacing: 0.3px; margin-bottom: 16px; }
  .about p { font-size: 10.2px; line-height: 14.9px; margin-bottom: 15px; }
  .consult-btn { position: absolute; left: 372px; top: 445px; width: 170px; height: 29px; background: var(--brand-blue); color: var(--white); font-size: 9px; font-weight: 600; letter-spacing: 1.1px; display: flex; align-items: center; justify-content: center; text-transform: uppercase; }

  .history-title { position: absolute; left: 0; top: 603px; width: 1015px; text-align: center; font-size: 21px; font-weight: 500; color: var(--ink); }
  .history-grid { position: absolute; left: 68px; top: 658px; width: 880px; height: 420px; display: grid; grid-template-columns: repeat(3, 1fr); grid-template-rows: repeat(2, 1fr); }
  .partner { display: flex; align-items: center; justify-content: center; gap: 8px; padding: 0 20px; text-align: center; font-size: 14px; font-weight: 600; color: #4d4f54; line-height: 18px; border-right: 1px solid var(--divider); }
  .partner:nth-child(3n) { border-right: none; }
  .partner:nth-child(-n+3) { border-bottom: 1px solid var(--divider); }
  .partner-mark { flex: none; width: 14px; height: 14px; background: #4d4f54; }
  .partner-mark.round { border-radius: 50%; }

  .site-footer { position: absolute; left: 0; top: 1146px; width: 1015px; height: 54px; background: var(--footer-bg); color: var(--white); font-size: 11px; }
  .footer-square { position: absolute; left: 68px; top: 11px; width: 32px; height: 32px; background: var(--brand-blue); }
  .footer-info { position: absolute; left: 137px; top: 20px; display: flex; gap: 28px; }
  .footer-info .label { color: var(--brand-blue); }
  .to-top { position: absolute; left: 914px; top: 0; width: 33px; height: 54px; background: var(--white); display: flex; align-items: center; justify-content: center; }
</style>
</head>
<body>
<div class="page">
  <header class="site-header">
    <div class="brand">
      <span class="brand-square"></span>
      <span class="brand-name">Civic<br>Lantern<br>Advisors</span>
    </div>
    <nav class="main-nav">
      <a class="is-active" href="#">About Us</a>
      <a href="#">Services &amp; Testimonials</a>
      <a href="#">Media &amp; Impact</a>
    </nav>
    <a class="contact-btn">Contact Us</a>
  </header>

  <div class="accent-block"></div>
  <div class="founder-photo" role="img" aria-label="Portrait photo of founder Mara Lin"></div>

  <section class="about">
    <h1>About&nbsp; Us</h1>
    <p>Civic Lantern Advisors supports nonprofit organizations and educational institutions to carry out their missions to benefit the wider community.</p>
    <p>Founder Mara Lin is an educator with a 22-year record of demonstrated achievement and leadership roles in nonprofits and educational institutions. Most recently, she served as Associate Dean of Students in the University and Director of the Lakeshore Community Service Center at Lakeshore University. Mara has designed, implemented, and evaluated community-based learning and leadership training programs that have attained positive outcomes documented by survey results, recognition by outside agencies, and grants awarded for new initiatives and expansions. She has also significantly and consistently increased the number of program applicants, volunteers, and community partnerships through innovative programming, improved reputation, targeted recruitment, marketing and communications.</p>
    <p>Mara is a native Chicagoan and has also lived in Tokyo, Boston, San Francisco, and Washington, DC. Mara received her bachelor of arts from Pinecrest College in Ashford, MN and her masters in education from Bayview University in Harborton, MA.</p>
  </section>
  <a class="consult-btn">Book a Consultation</a>

  <h2 class="history-title">Work History</h2>
  <div class="history-grid">
    <div class="partner"><span class="partner-mark"></span>Lakeshore Community Service Center</div>
    <div class="partner"><span class="partner-mark round"></span>Meridian Leaders Northern California</div>
    <div class="partner">Summit Path Bay Area Public Schools</div>
    <div class="partner"><span class="partner-mark"></span>Neighbor Schools</div>
    <div class="partner"><span class="partner-mark round"></span>ServeNation Volunteers</div>
    <div class="partner">Kite Exchange &amp; Teaching Program</div>
  </div>

  <footer class="site-footer">
    <span class="footer-square"></span>
    <div class="footer-info">
      <span>© 2019 <span class="label">Civic Lantern Advisors.</span>&nbsp; All Rights Reserved.</span>
      <span><span class="label">Phone:</span> (415) 555-0148</span>
      <span><span class="label">Email:</span> mara@civiclanternadvisors.com</span>
    </div>
    <a class="to-top" aria-label="Back to top">
      <svg width="12" height="13" viewBox="0 0 12 13"><path d="M6 0 L12 13 L6 10 L0 13 Z" fill="#4a9ad6"/></svg>
    </a>
  </footer>
</div>
</body>
</html>
```